Business Card New Design for Corvella

We would like a new look on our business card, using the same style, the same colors blue, gray and white with similar font that is represented on the new Sell Sheet. We recently re-designed our Sell Sheets - I've attached a sell sheet file for your reference. I've also attached our current business card and our logo. Keep the same information listed on each side of the card.

Contact Information for Business Card

Use details given on example provided

Font styles to use
Other font styles liked:
• Myriad Regular and Bold

Colors

Designer to choose colors to be used in the design.

Requirements
Must have
• Current Information that was provided on the current business card. Colors Must use Blue, Gray and White, the same colors as the sell sheet example.

```html
<!DOCTYPE html>
<html lang="en">
<head>
<meta charset="utf-8">
<title>Corvella Business Card</title>
<link href="https://fonts.googleapis.com/css2?family=Source+Sans+3:wght@400;600;700&display=swap" rel="stylesheet">
<style>
  :root {
    --page-bg: #2a2c2f;
    --blue: #1d4f9e;
    --blue-deep: #0f4594;
    --blue-bright: #0a6fc0;
    --gray-text: #2b2b2b;
    --silver-1: #bfc2c5;
    --silver-2: #eceded;
    --silver-3: #aeb1b4;
    --white: #ffffff;
  }
  * { box-sizing: border-box; margin: 0; padding: 0; }
  html, body { width: 1200px; height: 900px; overflow: hidden; }
  body {
    background: var(--page-bg);
    font-family: "Source Sans 3", "Myriad Pro", sans-serif;
    display: flex; flex-direction: column; align-items: center; justify-content: center; gap: 40px;
  }
  .card { position: relative; width: 700px; height: 400px; overflow: hidden; }

  /* Front */
  .card--front {
    background: linear-gradient(120deg, var(--silver-3) 0%, var(--silver-2) 45%, var(--silver-1) 100%);
    color: var(--gray-text);
  }
  .brand-name {
    position: absolute; top: 58px; right: 70px;
    font-size: 74px; font-weight: 700; letter-spacing: 10px; color: #4a4b4d; line-height: 1;
  }
  .brand-tagline {
    position: absolute; top: 146px; right: 76px;
    font-size: 24px; font-weight: 600; color: var(--blue);
  }
  .divider { position: absolute; top: 206px; left: 30px; width: 640px; height: 2px; background: var(--blue); }
  .person { position: absolute; top: 172px; left: 370px; text-align: center; width: 200px; }
  .person__name { font-size: 26px; font-weight: 700; color: var(--blue); line-height: 1; font-style: italic; }
  .person__role {
    position: absolute; top: 212px; left: 440px; background: var(--silver-2);
    padding: 0 8px; font-size: 16px; color: var(--gray-text);
  }
  .contact-list { position: absolute; top: 250px; left: 40px; list-style: none; font-size: 19px; line-height: 30px; }
  .contact-list li { display: flex; align-items: center; gap: 10px; }
  .contact-list svg { width: 18px; height: 18px; fill: var(--blue); flex: none; }
  .address { position: absolute; right: 40px; bottom: 36px; text-align: right; font-size: 19px; line-height: 27px; }

  /* Back */
  .card--back {
    background: radial-gradient(ellipse at 60% 60%, var(--blue-bright) 0%, var(--blue-deep) 70%);
    color: var(--white); text-align: center;
  }
  .back-name {
    margin-top: 52px; font-size: 92px; font-weight: 700; letter-spacing: 14px; line-height: 1;
  }
  .service-list {
    margin: 36px auto 0; width: 620px; font-size: 19px; font-weight: 600;
    text-transform: uppercase; line-height: 27px; letter-spacing: 0.3px;
  }
</style>
</head>
<body>
  <section class="card card--front" aria-label="Card front">
    <div class="brand-name">CORVELLA</div>
    <div class="brand-tagline">Corvella Technical Services, Inc.</div>
    <div class="divider"></div>
    <div class="person"><div class="person__name">MARTIN HALE</div></div>
    <div class="person__role">CEO</div>
    <ul class="contact-list">
      <li><svg viewBox="0 0 24 24"><path d="M3 9c0-3 4-5 9-5s9 2 9 5l-3 2-3-2V8H9v1l-3 2zM6 12h12l2 8H4z"/></svg>(888) 555-0142 226 Toll Free</li>
      <li><svg viewBox="0 0 24 24"><path d="M6 2l4 4-2 3c1 3 4 6 7 7l3-2 4 4-3 4C10 22 2 14 2 5z"/></svg>(815) 555-0178</li>
      <li><svg viewBox="0 0 24 24"><path d="M6 2l4 4-2 3c1 3 4 6 7 7l3-2 4 4-3 4C10 22 2 14 2 5z"/></svg>(815) 555-0193 (Direct)</li>
      <li><svg viewBox="0 0 24 24"><path d="M7 1h10a2 2 0 012 2v18a2 2 0 01-2 2H7a2 2 0 01-2-2V3a2 2 0 012-2zm0 3v14h10V4z"/></svg>(815) 555-0126</li>
    </ul>
    <address class="address" style="font-style:normal">
      4817 Harbor Mill Road<br>Lakemont, IL 60999<br>www.corvella-ts.com<br>mhale@corvella-ts.com
    </address>
  </section>

  <section class="card card--back" aria-label="Card back">
    <div class="back-name">CORVELLA</div>
    <p class="service-list">
      Conveyors • Target Suce Applicators<br>
      • Target Topping Applicators<br>
      • Waterfall Topping Applicators • Pepperoni<br>
      • Meat Slicer • Applicators<br>
      • Portion Controlled Filler Pumps<br>
      • Dry Ingredient Applicators<br>
      Check Weigh Conveyors • Portion Compensators
    </p>
  </section>
</body>
</html>
```